Pelican Media Website Design

Home page & interior page design.

Target Market(s)

Small businesses or at home businesses. Budget $1,000 - $3,000.

Industry/Entity Type

Media

Number of Pages Required

2 pages

Requirements
Must have
• Home page must consist of:
- Logo in top left
- Bannerimagery showcasing design examples (to be provided)
- 4 main modules, directing users to the 4 main product areas:
1. Templated brochure websites
2. Custom designed brochure websites
3. eCommerce websites
4. SEO

Area for text to be inserted (around 200 words) of introductory text

- Use of correct colour pallette based on logo provided
Nice to have
• Custom designed icons for the 4 main product areas.
Should not have
• Unstructured, cluttered layout

```html
<!DOCTYPE html>
<html lang="en">
<head>
<meta charset="utf-8">
<title>Pelican Media – Templated brochure websites</title>
<link rel="stylesheet" href="https://fonts.googleapis.com/css2?family=Baloo+2:wght@700;800&family=PT+Sans:wght@700&family=Source+Code+Pro:wght@700&display=swap">
<style>
  :root {
    --red: #d52027;
    --orange: #f0821e;
    --yellow: #f5c41c;
    --tab-text: #3a2a10;
    --ink: #1b1b1b;
    --white: #ffffff;
  }
  * { margin: 0; padding: 0; box-sizing: border-box; }
  html, body { width: 1200px; height: 800px; overflow: hidden; background: var(--white); }
  body { position: relative; font-family: "PT Sans", sans-serif; color: var(--ink); }

  .brand {
    position: absolute; left: 16px; top: 22px;
    display: flex; align-items: center; gap: 14px;
    font-family: "Baloo 2", sans-serif; font-weight: 800;
    font-size: 58px; line-height: 1; color: var(--orange);
  }
  .brand-mark { width: 26px; height: 26px; border-radius: 50%; background: var(--red); }

  .main-nav {
    position: absolute; left: 600px; top: 90px;
    display: flex; gap: 2px;
  }
  .main-nav a {
    display: block; width: 138px; height: 32px; padding-top: 7px;
    background: var(--yellow); border-radius: 12px 12px 0 0;
    text-align: center; text-decoration: none;
    font-size: 18px; color: var(--tab-text);
  }
  .header-rule { position: absolute; left: 0; top: 120px; width: 1200px; height: 8px; background: var(--red); }

  .hover-note {
    position: absolute; left: 91px; top: 133px;
    font-family: "Baloo 2", sans-serif; font-weight: 700; font-size: 21px; color: var(--red);
  }

  .product-band { position: absolute; left: 0; top: 175px; width: 1200px; height: 76px; }
  .product-band .band-orange { position: absolute; inset: 0 0 auto 0; height: 20px; background: var(--orange); }
  .product-band .band-red { position: absolute; left: 0; right: 0; top: 20px; height: 56px; background: var(--red); }

  .product-icon { position: absolute; top: 143px; width: 96px; height: 110px; }
  .product-label {
    position: absolute; color: var(--white);
    font-family: "Baloo 2", sans-serif; font-weight: 700; font-size: 21px; line-height: 26px;
  }

  .section-title {
    position: absolute; left: 27px; top: 284px;
    font-family: "Baloo 2", sans-serif; font-weight: 700; font-size: 25px; color: var(--red);
  }
  .intro-text {
    position: absolute; left: 27px; top: 328px; width: 1150px;
    font-family: "Source Code Pro", monospace; font-weight: 700; font-size: 13.6px; line-height: 19px;
    white-space: nowrap; overflow: hidden;
  }

  .design-sample { position: absolute; box-shadow: 0 0 0 1px #c9c9c9; }
  .sample-1 { left: 76px; top: 445px; width: 203px; height: 203px; background: linear-gradient(135deg, #1a1016, #7a1e5a 45%, #e07b1a 75%, #1a1016); }
  .sample-2 { left: 324px; top: 445px; width: 203px; height: 194px; background: linear-gradient(180deg, #2b3440, #5b7490 35%, #273039 60%, #1c232b); }
  .sample-3 { left: 583px; top: 443px; width: 201px; height: 221px; background: linear-gradient(180deg, #b0241a 0 22%, #f7f3ee 22% 62%, #e0661a 62% 80%, #f7f3ee 80%); }
  .sample-4 { left: 844px; top: 443px; width: 205px; height: 226px; background: linear-gradient(180deg, #2d8fc8, #8cc63f 28%, #f3f7f2 30%, #e8f1f5); }

  .design-caption {
    position: absolute; top: 700px; width: 160px; text-align: center;
    font-size: 16px; color: var(--ink);
  }
</style>
</head>
<body>

<header>
  <div class="brand"><span>Pelican Media</span><span class="brand-mark"></span></div>
  <nav class="main-nav">
    <a href="#">Home</a>
    <a href="#">Servcies</a>
    <a href="#">Portfolio</a>
    <a href="#">Contact Us</a>
  </nav>
  <div class="header-rule"></div>
</header>

<p class="hover-note">On Mouse over</p>

<section class="product-band" aria-label="Product areas">
  <div class="band-orange"></div>
  <div class="band-red"></div>
</section>

<!-- Templated brochure websites -->
<svg class="product-icon" style="left:-4px" viewBox="0 0 96 110" aria-hidden="true">
  <polygon points="3,4 93,4 48,106" fill="var(--orange)" stroke="var(--white)" stroke-width="4" stroke-linejoin="round"/>
  <rect x="26" y="18" width="28" height="24" fill="none" stroke="var(--white)" stroke-width="3"/>
  <rect x="38" y="30" width="28" height="24" fill="var(--orange)" stroke="var(--white)" stroke-width="3"/>
</svg>
<p class="product-label" style="left:91px; top:196px">Templated<br>brochure websites</p>

<!-- Custom designed brochure websites -->
<svg class="product-icon" style="left:276px" viewBox="0 0 96 110" aria-hidden="true">
  <polygon points="3,4 93,4 48,106" fill="var(--orange)" stroke="var(--white)" stroke-width="4" stroke-linejoin="round"/>
  <path d="M34 20 l0 36 M28 20 a6 6 0 0 0 12 0" fill="none" stroke="var(--white)" stroke-width="4" stroke-linecap="round"/>
  <path d="M60 26 l0 30 M52 22 h16 v8 h-16 z" fill="var(--white)" stroke="var(--white)" stroke-width="4" stroke-linejoin="round"/>
</svg>
<p class="product-label" style="left:368px; top:201px">Custom designed<br>brochure websites</p>

<!-- eCommerce websites -->
<svg class="product-icon" style="left:598px" viewBox="0 0 96 110" aria-hidden="true">
  <polygon points="3,4 93,4 48,106" fill="var(--orange)" stroke="var(--white)" stroke-width="4" stroke-linejoin="round"/>
  <path d="M24 22 h8 l6 24 h24 l5 -16 h-33" fill="none" stroke="var(--white)" stroke-width="3.5" stroke-linejoin="round"/>
  <circle cx="41" cy="53" r="3.5" fill="var(--white)"/>
  <circle cx="59" cy="53" r="3.5" fill="var(--white)"/>
</svg>
<p class="product-label" style="left:693px; top:202px">eCommerce websites</p>

<!-- SEO -->
<svg class="product-icon" style="left:908px" viewBox="0 0 96 110" aria-hidden="true">
  <polygon points="3,4 93,4 48,106" fill="var(--orange)" stroke="var(--white)" stroke-width="4" stroke-linejoin="round"/>
  <circle cx="44" cy="34" r="14" fill="none" stroke="var(--white)" stroke-width="3.5"/>
  <path d="M30 34 h28 M44 20 v28 M36 23 q-5 11 0 22 M52 23 q5 11 0 22" fill="none" stroke="var(--white)" stroke-width="2"/>
  <path d="M54 44 l12 12" stroke="var(--white)" stroke-width="5" stroke-linecap="round"/>
</svg>
<p class="product-label" style="left:998px; top:206px">SEO</p>

<main>
  <h1 class="section-title">Templated brochure websites</h1>
  <p class="intro-text">jdashgdhsghldshgjhdfsflkdsjgkljskldgjkldfsjgkljdgkldsjklgjskldjgsdgkjfkldsnklgnkldsngklnsdlfgfhmdsgkjkjkfjkfdjklkldfnkldfklhfdkdsgkfjkjfdk<br>jkfdjkhjfkh;ldfk;glbghgffffffffffffffffkas;lkfa[wlf;ads,.leg[pelgsk’dfs,lgpaoed]-[FLDAS,C.Z,X;CJfy9wepogkdf,nmgvkjdhfvueugtpfoewkdsg.<br>jdashgdhsghldshgjhdfsflkdsjgkljskldgjkldfsjgkljdgkldsjklgjskldjgsdgkjfkldsnklgnkldsngklnsdlfgfhmdsgkjkjkfjkfdjklkldfnkldfklhfdkdsgkfjkjfdk<br>jkfdjkhjfkh;ldfk;glbghgffffffffffffffffkas;lkfa[wlf;ads,.leg[pelgsk’dfs,lgpaoed]-[FLDAS,C.Z,X;CJfy9wepogkdf,nmgvkjdhfvueugtpfoewkdsg.</p>

  <div class="design-sample sample-1" role="img" aria-label="Website template preview: dark page with colourful swirling waves"></div>
  <div class="design-sample sample-2" role="img" aria-label="Website template preview: dark business layout with a globe banner"></div>
  <div class="design-sample sample-3" role="img" aria-label="Website template preview: red and white layout with orange feature block"></div>
  <div class="design-sample sample-4" role="img" aria-label="Website template preview: blue and green layout with sky banner"></div>

  <p class="design-caption" style="left:104px">Design1</p>
  <p class="design-caption" style="left:328px">Design2</p>
  <p class="design-caption" style="left:601px">Design3</p>
  <p class="design-caption" style="left:857px">Design4</p>
</main>

</body>
</html>
```